Horse related business entrepreneur needs a business card

I need a business card design for my horse related business. The enterprise is Copper Vale LLC and I have 3 businesses (headquartered at 2 locations): 1. property management where we rent horse stalls and apartments at a thoroughbred training center outside Ocala; 2. a medium sized transportation service in central Florida that sells horse bedding and removes used horse bedding from horse farms; and horse racing

```html
<!DOCTYPE html>
<html lang="en">
<head>
<meta charset="utf-8">
<title>Copper Vale LLC – Business Card</title>
<link rel="stylesheet" href="https://fonts.googleapis.com/css2?family=Cinzel:wght@500;600&family=Lato:wght@400&display=swap">
<style>
  :root {
    --stage: #e9e6e1;
    --card-blue: #436380;
    --card-white: #ffffff;
    --ink-light: #ffffff;
    --brand-blue: #3f5f7c;
    --rule: rgba(255,255,255,0.85);
    --shadow: 0 4px 8px rgba(0,0,0,0.35);
  }
  html, body {
    margin: 0;
    padding: 0;
    width: 1200px;
    height: 900px;
    overflow: hidden;
    background: var(--stage);
  }
  .canvas {
    position: relative;
    width: 1200px;
    height: 900px;
  }
  .card {
    position: absolute;
    box-shadow: var(--shadow);
    box-sizing: border-box;
  }
  .card--front {
    left: 330px;
    top: 90px;
    width: 555px;
    height: 343px;
    background: var(--card-blue);
    color: var(--ink-light);
    font-family: "Lato", Arial, sans-serif;
    text-align: center;
  }
  .card--back {
    left: 330px;
    top: 470px;
    width: 560px;
    height: 342px;
    background: var(--card-white);
  }
  .holder-name {
    position: absolute;
    left: 0; right: 0;
    top: 54px;
    margin: 0;
    font-family: "Cinzel", Georgia, serif;
    font-weight: 600;
    font-size: 25px;
    letter-spacing: 0.5px;
    line-height: 1;
  }
  .holder-role {
    position: absolute;
    left: 0; right: 0;
    top: 80px;
    font-size: 15px;
    line-height: 1;
  }
  .divider {
    position: absolute;
    left: 0;
    width: 555px;
    height: 20px;
  }
  .divider--contact { top: 112px; }
  .divider--address { top: 213px; }
  .contact-list {
    position: absolute;
    left: 0; right: 0;
    top: 141px;
    margin: 0;
    padding: 0;
    list-style: none;
    font-size: 16px;
    line-height: 20.5px;
  }
  .address-list {
    position: absolute;
    left: 0; right: 0;
    top: 244px;
    margin: 0;
    padding: 0;
    list-style: none;
    font-size: 16px;
    line-height: 26px;
  }
  .brand {
    position: absolute;
    left: 0; right: 0;
    top: 0; bottom: 0;
    display: flex;
    flex-direction: column;
    align-items: center;
    justify-content: center;
    gap: 26px;
    padding-top: 10px;
  }
  .brand-square {
    width: 120px;
    height: 110px;
    border: 5px solid var(--brand-blue);
    box-sizing: border-box;
  }
  .brand-name {
    font-family: "Cinzel", Georgia, serif;
    font-weight: 600;
    font-size: 28px;
    color: var(--brand-blue);
    letter-spacing: 0.5px;
    line-height: 1;
  }
</style>
</head>
<body>
<main class="canvas">
  <section class="card card--front" aria-label="Card front">
    <h1 class="holder-name">Dale Whitcomb</h1>
    <div class="holder-role">Owner</div>

    <svg class="divider divider--contact" viewBox="0 0 555 20" aria-hidden="true">
      <line x1="188" y1="10" x2="240" y2="10" stroke="var(--rule)" stroke-width="1"/>
      <line x1="316" y1="10" x2="368" y2="10" stroke="var(--rule)" stroke-width="1"/>
      <rect x="243" y="1" width="19" height="18" fill="#fff"/>
      <path d="M246 9 q6.5 -6 13 0 l-2 2 l-2 -1.5 v-1.5 h-5 v1.5 l-2 1.5z" fill="var(--card-blue)"/>
      <rect x="248" y="11" width="9" height="5" fill="var(--card-blue)"/>
      <rect x="267" y="1" width="19" height="18" fill="#fff"/>
      <rect x="271" y="4" width="11" height="4" fill="var(--card-blue)"/>
      <rect x="269.5" y="8.5" width="14" height="6" fill="var(--card-blue)"/>
      <rect x="272" y="12" width="9" height="5" fill="var(--card-blue)" stroke="#fff" stroke-width="1"/>
      <rect x="291" y="1" width="19" height="18" fill="#fff"/>
      <rect x="294" y="5.5" width="13" height="9" fill="var(--card-blue)"/>
      <path d="M294.5 6 l6 5 l6 -5" fill="none" stroke="#fff" stroke-width="1"/>
    </svg>

    <ul class="contact-list">
      <li>(555) 201-0172</li>
      <li>(555) 201-0148</li>
      <li>dale@coppervale.com</li>
    </ul>

    <svg class="divider divider--address" viewBox="0 0 555 20" aria-hidden="true">
      <line x1="188" y1="10" x2="265" y2="10" stroke="var(--rule)" stroke-width="1"/>
      <line x1="290" y1="10" x2="367" y2="10" stroke="var(--rule)" stroke-width="1"/>
      <rect x="268" y="1" width="19" height="18" fill="#fff"/>
      <path d="M277.5 16 l-4 -6 a4.5 4.5 0 1 1 8 0z" fill="var(--card-blue)"/>
      <circle cx="277.5" cy="8" r="1.6" fill="#fff"/>
    </svg>

    <ul class="address-list">
      <li>2615 SE 131st Lane&nbsp; Pinecrest Hollow, FL 30571</li>
      <li>718 Millbrook Ridge Road Ashford Glen, NV 80914</li>
    </ul>
  </section>

  <section class="card card--back" aria-label="Card back">
    <div class="brand">
      <div class="brand-square" aria-hidden="true"></div>
      <div class="brand-name">Copper Vale LLC</div>
    </div>
  </section>
</main>
</body>
</html>
```